Trifold - Gentle Horizon Therapy

Marianne Dobbs, Psy.D.Licensed Psychologist

this is for hypnosis and meditation
I like decorative font for my name (conservative decorative)

calming effect is most imortant

Target Market(s)

clients with depression, pain, anxiety - adults and aged

Industry/Entity Type

Conservative

Font styles to use
Serif

Colors
abd037
85cae6
cadf82
34a7d7
ffffff
886aae
6b449b

Requirements
Must have
• I like zen-like calming effects. lime Green, light blues and purple. I like waves and color.
• I like water and light, flowers and plants - bamboo, stacking rocks, ocean, water, lotus flowers
Should not have
• not too much purple
• Mostly green and blue

```html
<!DOCTYPE html>
<html lang="en">
<head>
<meta charset="utf-8">
<title>Gentle Horizon Therapy – Trifold</title>
<link rel="stylesheet" href="https://fonts.googleapis.com/css2?family=Petit+Formal+Script&family=Raleway:ital,wght@0,300;0,400;0,500;0,600;0,700;0,800;1,400;1,500;1,600&display=swap">
<style>
:root{
  --stage:#d6d6d6;
  --lime:#abd037;
  --lime-soft:#cadf82;
  --sky:#85cae6;
  --blue:#34a7d7;
  --blue-deep:#1a5f9f;
  --navy:#1e4f8f;
  --purple:#6b449b;
  --purple-soft:#886aae;
  --white:#ffffff;
  --ink:#7a7a7a;
  --ink-dark:#4d4d4d;
  --script:"Petit Formal Script", cursive;
  --sans:"Raleway", sans-serif;
}
*{box-sizing:border-box;margin:0;padding:0}
html,body{width:757px;height:1200px;overflow:hidden;background:var(--stage)}
.canvas{position:relative;width:757px;height:1200px;background:var(--stage);font-family:var(--sans)}
.sheet{position:absolute;left:45px;width:668px;background:var(--white);overflow:hidden;box-shadow:0 10px 18px rgba(0,0,0,.22)}
.sheet--outside{top:52px;height:513px}
.sheet--inside{top:618px;height:515px}
.waves{position:absolute;inset:0;width:100%;height:100%}
.panel{position:absolute;top:0;height:100%;width:222.7px}
.panel--1{left:0}.panel--2{left:222.7px}.panel--3{left:445.3px}
.abs{position:absolute}
.photo{position:absolute}

/* outside, panel 1 */
.services-bg{left:0;top:0;width:223px;height:420px;background:linear-gradient(180deg,#eef3ea 0%,#f7f9f4 45%,#ffffff 80%)}
.services-title{left:14px;top:14px;font-family:var(--script);color:var(--lime);font-size:19px;line-height:1}
.services-sub{left:14px;top:38px;color:var(--ink-dark);font-size:13px;font-weight:400}
.service{left:14px;width:190px}
.service h3{color:var(--navy);font-size:9.6px;font-weight:500;line-height:1.2;margin-bottom:4px}
.service p{color:var(--ink);font-size:7.6px;line-height:1.3;text-align:justify;font-weight:400}
.fee{left:14px;top:488px;width:200px;color:var(--white);font-size:7.8px;font-weight:500;line-height:1.3}

/* outside, panel 2 */
.water{left:0;top:0;width:223px;height:200px;background:linear-gradient(180deg,#4fb3d2 0%,#7fcbe0 45%,#cfeaf2 78%,#ffffff 100%)}
.name-center{left:0;width:223px;text-align:center}
.name{font-family:var(--script);color:var(--navy);font-size:19px;white-space:nowrap}
.name small{font-family:var(--sans);font-size:10px;font-weight:400}
.licensed{color:var(--ink-dark);font-size:8.4px;font-weight:400}
.motto{font-family:var(--script);color:var(--navy);font-size:12px;line-height:1.45}
.office{color:var(--navy);font-size:9.6px;font-weight:500}
.venue{color:var(--ink-dark);font-size:9px;font-weight:600;letter-spacing:2px;text-transform:uppercase}
.address{color:var(--ink-dark);font-size:8px;line-height:1.3}
.phone-line{color:var(--navy);font-size:14px;font-weight:700;display:flex;align-items:center;justify-content:center;gap:6px}
.lotus-pair{left:-8px;top:380px;width:90px;height:112px;border-radius:40% 40% 10% 10%;background:radial-gradient(ellipse at 55% 40%,#f6b9d6 0%,#ec8fbd 35%,rgba(236,143,189,0) 72%)}
.web-pill{height:14px;border-radius:8px;background:var(--lime-soft);color:var(--navy);font-size:9px;font-weight:500;display:flex;align-items:center;justify-content:center}
.web-pill b{font-weight:700}

/* outside, panel 3 */
.cover-photo{left:0;top:0;width:223px;height:360px;background:radial-gradient(ellipse at 60% 62%,#f8d7e6 0%,#e9a8c8 14%,rgba(233,168,200,0) 30%),linear-gradient(160deg,#8fce6a 0%,#4c9e3a 40%,#2f7d2c 75%,#3f8f35 100%)}
.cover-motto{left:0;top:36px;width:223px;text-align:center;font-family:var(--script);color:var(--white);font-size:12.6px;line-height:1.45}
.cover-name{left:0;top:372px;width:223px;text-align:center;color:var(--white)}
.cover-name .name{color:var(--white);font-size:20px}
.cover-name .licensed{color:var(--white);font-size:9.6px}
.speciality{left:0;top:424px;width:223px;text-align:center;color:var(--white);font-size:11.6px;line-height:1.15}
.speciality b{font-weight:800}
.cover-rule{left:28px;top:449px;width:166px;height:1px;background:rgba(255,255,255,.8)}
.cover-phone{left:0;top:453px;width:223px;text-align:center;color:var(--white);font-size:19px;font-weight:500}

/* inside, panel 1 */
.what-title{left:14px;top:16px;color:var(--navy);font-size:15.5px;font-weight:400;line-height:1.1}
.what-title span{display:block;font-family:var(--script);color:var(--lime);font-size:14.2px;line-height:1.3}
.body-copy{color:var(--ink);font-size:7.6px;line-height:1.31;text-align:justify}
.bamboo{left:105px;top:232px;width:118px;height:185px;background:radial-gradient(ellipse at 60% 60%,#7fb845 0%,#a9d176 40%,rgba(210,232,180,0) 75%)}
.effective{left:14px;top:300px;width:130px;color:var(--navy);font-size:9.8px;font-weight:700;line-height:1.3}
.issues{left:14px;top:417px;list-style:none;color:var(--white);font-size:7.8px;line-height:1.32}
.issues li::before{content:"• "}

/* inside, panel 2 */
.purple-head{color:var(--purple);font-size:10.8px;font-weight:700;line-height:1.3;text-transform:uppercase}
.sub-head{color:var(--purple);font-size:9.4px;font-weight:600}
.italic-head{color:var(--purple);font-size:9.4px;font-style:italic;font-weight:600}
.goal-list{list-style:none;color:var(--purple-soft);font-size:6.8px;font-style:italic;line-height:1.35}
.goal-list li::before{content:"• "}
.stones{left:150px;top:415px;width:70px;height:95px;border-radius:40% 40% 20% 20%;background:radial-gradient(ellipse at 50% 45%,#8c8c8c 0%,#b9b9b9 40%,rgba(220,220,220,0) 75%)}

/* inside, panel 3 */
.name-badge{left:28px;top:28px;width:160px;height:21px;border-radius:11px;background:linear-gradient(180deg,var(--purple-soft),var(--purple));color:var(--white);font-family:var(--script);font-size:12.5px;display:flex;align-items:center;justify-content:center;box-shadow:0 2px 3px rgba(0,0,0,.2)}
.portrait{left:10px;top:236px;width:213px;height:279px;background:radial-gradient(ellipse at 55% 45%,#e9d3bd 0%,#cfb79e 28%,#a9d8d6 55%,rgba(255,255,255,0) 80%)}
</style>
</head>
<body>
<div class="canvas">

  <!-- Outside of the trifold -->
  <section class="sheet sheet--outside">
    <div class="photo services-bg" role="img" aria-label="Faint photo of calm water and stacked stones"></div>
    <div class="photo water" role="img" aria-label="Photo of clear rippling blue water"></div>
    <div class="photo cover-photo" role="img" aria-label="Photo of a pink lotus flower on green leaves" style="left:445.3px"></div>

    <svg class="waves" viewBox="0 0 668 513" preserveAspectRatio="none" aria-hidden="true">
      <defs>
        <linearGradient id="blueBand" x1="0" y1="0" x2="0" y2="1">
          <stop offset="0" stop-color="#34a7d7"/><stop offset="1" stop-color="#1a5f9f"/>
        </linearGradient>
        <linearGradient id="limeBand" x1="0" y1="0" x2="1" y2="0">
          <stop offset="0" stop-color="#cadf82"/><stop offset="1" stop-color="#abd037"/>
        </linearGradient>
      </defs>
      <!-- panel 1 -->
      <path d="M0 383 C70 378 150 415 223 450 L223 513 L0 513Z" fill="url(#limeBand)"/>
      <path d="M0 438 C80 430 160 448 223 468 L223 513 L0 513Z" fill="#fff"/>
      <path d="M0 446 C80 438 160 456 223 476 L223 513 L0 513Z" fill="url(#blueBand)"/>
      <!-- panel 2 -->
      <path d="M223 478 C300 462 380 400 445.3 345 L445.3 513 L223 513Z" fill="url(#limeBand)"/>
      <path d="M223 505 C300 480 380 420 445.3 365 L445.3 513 L223 513Z" fill="#fff"/>
      <path d="M223 513 C300 488 380 428 445.3 372 L445.3 513Z" fill="url(#blueBand)"/>
      <!-- panel 3 -->
      <path d="M445.3 338 C520 318 600 300 668 296 L668 513 L445.3 513Z" fill="url(#limeBand)"/>
      <path d="M445.3 358 C530 338 600 326 668 326 L668 513 L445.3 513Z" fill="#fff"/>
      <path d="M445.3 366 C530 346 600 334 668 334 L668 513 L445.3 513Z" fill="url(#blueBand)"/>
    </svg>

    <div class="panel panel--1">
      <h2 class="abs services-title">Psychological</h2>
      <p class="abs services-sub">Services</p>
      <div class="abs service" style="top:68px">
        <h3>Initial evaluation</h3>
        <p>Mental health assessment, diagnosis and comprehensive wellness planning.</p>
      </div>
      <div class="abs service" style="top:114px">
        <h3>Gentle Horizon Therapy (GHT)</h3>
        <p>Resolve emotional distress, heartbreak and grief. GHT clears trauma at the subconscious level with hypnotic communication. The most troubling of memories are worked through and clients gain a sense of clarity, peace and power. Only a couple of sessions are needed to experience dramatic and long-lasting effects.</p>
      </div>
      <div class="abs service" style="top:207px">
        <h3>Eye Movement Desensitization and Reprocessing (EMDR)</h3>
        <p>Evidence-based treatment for post-traumatic stress disorder, anxiety, depression and adverse experiences. Experience relief and empowerment. More information at emdrguide.org.</p>
      </div>
      <div class="abs service" style="top:282px">
        <h3>Short-term talk therapy</h3>
        <p>Psychotherapy to create a more satisfying life. Proactive approach to seeking effective solutions for your most pressing emotional and relational problems.</p>
      </div>
      <div class="abs service" style="top:350px">
        <h3>Meditation for Wellness</h3>
        <p>Personalized meditation for calm, healing and well-being.</p>
      </div>
      <p class="abs fee">Fee Information: Major insurance plans accepted and filed.</p>
    </div>

    <div class="panel panel--2">
      <div class="abs name-center" style="top:146px">
        <div class="name">Marianne Dobbs, <small>Psy.D.</small></div>
        <div class="licensed">Licensed Psychologist</div>
      </div>
      <p class="abs name-center motto" style="top:192px">Heal the Past<br>Embrace the Present<br>Create the Future</p>
      <svg class="abs" style="left:105px;top:261px" width="12" height="14" viewBox="0 0 12 14" aria-hidden="true">
        <path d="M6 0C2.7 0 0 2.6 0 5.8 0 10 6 14 6 14s6-4 6-8.2C12 2.6 9.3 0 6 0Z" fill="#abd037"/>
        <circle cx="6" cy="5.6" r="2.2" fill="#fff"/>
      </svg>
      <p class="abs name-center office" style="top:277px">Office Location:</p>
      <p class="abs name-center venue" style="top:294px">Stillwater Wellness Center</p>
      <p class="abs name-center address" style="top:314px">Coral Plaza<br>2280 Seabreeze Ave #14<br>Harbor Point, FL &nbsp;32999</p>
      <div class="abs name-center phone-line" style="top:352px">
        <svg width="13" height="13" viewBox="0 0 16 16" aria-hidden="true">
          <circle cx="8" cy="8" r="7.2" fill="none" stroke="#1e4f8f" stroke-width="1.4"/>
          <path d="M5.6 4.2 6.9 5.9 6 7c.5 1.1 1.3 1.9 2.4 2.4l1.1-.9 1.7 1.3-.8 1.4c-2.8-.3-5.2-2.7-5.5-5.5Z" fill="#1e4f8f"/>
        </svg>
        <span>321 555-0142</span>
      </div>
      <div class="photo lotus-pair" role="img" aria-label="Photo of two pink lotus flowers on tall stems"></div>
      <div class="abs web-pill" style="left:44px;top:492px;width:137px">www.<b>stillwaterhwc</b>.com</div>
    </div>

    <div class="panel panel--3">
      <p class="abs cover-motto">Unleashing the<br>Power of the Mind<br>for Healing and Well-being</p>
      <div class="abs cover-name">
        <div class="name">Marianne Dobbs, <small>Psy.D.</small></div>
        <div class="licensed">Licensed Psychologist</div>
      </div>
      <p class="abs speciality">Specializing in<br><b>adults</b> and <b>couples</b></p>
      <div class="abs cover-rule"></div>
      <p class="abs cover-phone">321 555-0142</p>
      <div class="abs web-pill" style="left:42px;top:492px;width:139px">www.<b>stillwaterhwc</b>.com</div>
    </div>
  </section>

  <!-- Inside of the trifold -->
  <section class="sheet sheet--inside">
    <div class="photo bamboo" role="img" aria-label="Photo of green bamboo stalks and leaves"></div>
    <div class="photo portrait" role="img" aria-label="Portrait photo of the psychologist" style="left:455px"></div>

    <svg class="waves" viewBox="0 0 668 515" preserveAspectRatio="none" aria-hidden="true">
      <defs>
        <linearGradient id="blueBand2" x1="0" y1="0" x2="0" y2="1">
          <stop offset="0" stop-color="#34a7d7"/><stop offset="1" stop-color="#1a5f9f"/>
        </linearGradient>
        <linearGradient id="limeBand2" x1="0" y1="0" x2="1" y2="0">
          <stop offset="0" stop-color="#cadf82"/><stop offset="1" stop-color="#abd037"/>
        </linearGradient>
      </defs>
      <!-- panel 1 -->
      <path d="M0 360 C80 348 160 372 223 398 L223 515 L0 515Z" fill="url(#limeBand2)"/>
      <path d="M0 388 C80 380 160 392 223 408 L223 515 L0 515Z" fill="#fff"/>
      <path d="M0 395 C80 388 160 400 223 415 L223 515 L0 515Z" fill="url(#blueBand2)"/>
      <!-- panel 2 -->
      <path d="M223 468 C300 452 380 466 445.3 478 L445.3 515 L223 515Z" fill="url(#limeBand2)"/>
      <path d="M223 480 C300 466 380 478 445.3 490 L445.3 515 L223 515Z" fill="#fff"/>
      <path d="M223 485 C300 472 380 484 445.3 495 L445.3 515 L223 515Z" fill="url(#blueBand2)"/>
      <!-- panel 3 -->
      <path d="M445.3 478 C520 470 600 476 668 470 L668 515 L445.3 515Z" fill="url(#limeBand2)"/>
      <path d="M445.3 492 C520 484 600 490 668 486 L668 515 L445.3 515Z" fill="url(#blueBand2)"/>
    </svg>
    <div class="photo stones" role="img" aria-label="Photo of stacked zen stones with a pink lotus" style="left:380px"></div>

    <div class="panel panel--1">
      <h2 class="abs what-title">What is<span>Gentle Horizon Therapy</span><span>(GHT)</span></h2>
      <p class="abs body-copy" style="left:14px;top:82px;width:186px">GHT dramatically enhances mood, creates calm, eases grief, optimizes health and promotes success. It is a form of hypnosis that clears stuck personal and interpersonal patterns at the subconscious level. Emotionally charged memories from the past are desensitized. You do not have to talk about your problems, share looping thoughts or re-experience painful emotions. Instead, you are guided to engage in deep brain processing to create an internal shift that changes automatic thoughts and feelings. Transformation happens within your nervous system and thereby facilitates lasting positive effects. Only one or two sessions are needed to experience symptom relief. Sessions are generally 1.5 – 2 hours long.</p>
      <p class="abs effective">GHT is effective for many of life's problems including:</p>
      <ul class="abs issues">
        <li>PTSD, Sexual Abuse and Childhood Abuse</li>
        <li>Grief, Infidelity and Heartbreak</li>
        <li>Relationship issues</li>
        <li>Anger and Resentment</li>
        <li>Guilt / Shame</li>
        <li>Anxiety / Fear</li>
        <li>Nightmares / Insomnia</li>
        <li>Stress-related symptoms and Pain</li>
      </ul>
    </div>

    <div class="panel panel--2">
      <h2 class="abs purple-head" style="left:12px;top:14px;width:205px">Clearing old stuff and making way for new beginnings</h2>
      <p class="abs body-copy" style="left:12px;top:48px;width:199px">If you have been unable to change how you feel, think or act, it is likely that you are being affected by experiences from your past. When something is highly distressing, it slams into awareness and leaves a lasting impression. Even when the experience is finished, deeper parts of the mind may continue to respond as if the distressing event is still occurring. Emotional problems, interpersonal difficulties and destructive behaviors are impossible to overcome when fueled by the ongoing influence of past events. You may consciously understand the value of changing a behavior, but unless your deeper mind is transformed, change is not likely. In GHT the subconscious mind is engaged, and the influence of past events is eliminated. Energy that was blocked is released and healing takes place. Negative habits and painful emotions are replaced by well-being, empowerment and productivity.</p>
      <h3 class="abs sub-head" style="left:12px;top:231px">What happens in a GHT Session?</h3>
      <p class="abs body-copy" style="left:12px;top:247px;width:199px">Trauma is stored in the mind and body. Through GHT, you will experience profound physiological calm and you will be guided towards emotional resolution in a gentle, creative and even humorous way. You access inner resources of light and wisdom. You step into the awareness of your true self. As Jonah Hale states: "we all have a beautiful light within, we just sometimes forget it is there". From this enlightened place, disturbing memories are easily reframed with new meaning. You will leave the session feeling peaceful and sourced from within by a free-flowing energy.</p>
      <h3 class="abs italic-head" style="left:12px;top:374px">Clear Your Mind and Change Your World</h3>
      <ul class="abs goal-list" style="left:12px;top:390px;width:200px">
        <li>Discover and resolve subconscious causes for emotional and behavioral difficulties</li>
        <li>Eliminate unconscious conflicts blocking desired change</li>
        <li>Promote mind / body healing</li>
      </ul>
    </div>

    <div class="panel panel--3">
      <div class="abs name-badge">Dr. Marianne Dobbs</div>
      <p class="abs body-copy" style="left:12px;top:64px;width:202px">Dr. Dobbs is a licensed clinical psychologist specializing in adults and seniors. She treats people for depression, anxiety, grief, sexual trauma, PTSD, relationship issues, infidelity, divorce and stress-related symptoms. She has over 20 years of clinical experience in mental health and is an adjunct counseling professor at Lakeside University. She received her Master's and Doctorate degrees in Clinical Psychology from Meridian University in Honolulu, Hawaii. She earned a Bachelor's of Science degree in Rehabilitation Medicine from Northgate University in Halvern, Canada. At Stillwater Wellness Center, she provides initial evaluations, assessment, diagnosis and comprehensive treatment planning. She will collaborate with you to create solutions for healing, empowerment and wellness.</p>
    </div>
  </section>

</div>
</body>
</html>
```